DOUBLE SIDED BROCHURE NEEDED TO PROMOTE DOCTOR

I need a double sided DL size (99mm x 210mm) brochure, promoting a doctor seeing patients in a new area.

I want something professional. I have included the relevant information. I would also like the Dr's picture somwhere in the brochure, with a professional background. I wish to print these tomorrow, so i will pick a winner within 14 hours of posting this ad.

I have included an example of a brochures design that I recently saw, and its definietly a good starting point.

Medical

```html
<!DOCTYPE html>
<html lang="en">
<head>
<meta charset="utf-8">
<title>Dr. Halden – Surgical Services</title>
<link href="https://fonts.googleapis.com/css2?family=Fondamento&family=Open+Sans:wght@400&display=swap" rel="stylesheet">
<style>
  :root {
    --brand-blue: #2f8fef;
    --deep-blue: #1b4ea0;
    --sky: #4fd3f8;
    --ink: #1e1e1e;
    --white: #ffffff;
  }
  * { margin: 0; padding: 0; box-sizing: border-box; }
  html, body { width: 1200px; height: 2535px; overflow: hidden; background: var(--white); }
  .brochure { position: relative; width: 1200px; height: 2535px; background: var(--white); overflow: hidden; font-family: "Open Sans", Arial, sans-serif; }

  .top-bar { position: absolute; left: 0; top: 0; width: 1200px; height: 30px; background: var(--brand-blue); }

  .intro { position: absolute; left: 73px; top: 120px; width: 1048px; font-family: Arial, Helvetica, sans-serif; font-weight: 700; font-size: 47px; line-height: 61px; color: var(--deep-blue); text-align: justify; text-align-last: left; }

  .specialties { position: absolute; left: 66px; top: 375px; width: 1060px; list-style: none; }
  .specialties li { position: relative; padding-left: 66px; font-size: 43px; line-height: 62px; color: var(--ink); margin-bottom: 62px; }
  .specialties li::before { content: ""; position: absolute; left: 2px; top: 30px; width: 17px; height: 17px; border-radius: 50%; background: var(--ink); }
  .specialties li.two-line { margin-bottom: 44px; }

  .stethoscope { position: absolute; left: 270px; top: 745px; width: 635px; height: 420px; border-radius: 40px; background: radial-gradient(ellipse at center, #3a5ee8 0%, #8fa4f0 45%, #ffffff 75%); }

  .surgery-panel { position: absolute; left: 0; top: 1190px; width: 1200px; height: 1345px; }
  .surgery-panel svg { position: absolute; left: 0; top: 0; }

  .panel-title { position: absolute; left: 0; top: 1255px; width: 1200px; text-align: center; font-family: "Fondamento", cursive; color: var(--white); font-size: 138px; line-height: 196px; }

  .procedures { position: absolute; left: 80px; top: 1705px; list-style: none; }
  .procedures li { position: relative; padding-left: 72px; font-size: 43px; line-height: 72px; color: var(--white); margin-bottom: 43px; }
  .procedures li::before { content: ""; position: absolute; left: 0; top: 30px; width: 16px; height: 16px; border-radius: 50%; background: var(--white); }

  .portrait { position: absolute; left: 776px; top: 1680px; width: 424px; height: 604px; border-radius: 200px 0 0 0; background: linear-gradient(180deg, #c7a88f 0%, #a98a75 40%, #1f2836 75%, #141a24 100%); }

  .name-plate { position: absolute; left: 88px; top: 2284px; width: 1112px; height: 206px; background: var(--white); border-radius: 42px 0 0 42px; }
  .name-plate .tab { position: absolute; left: 8px; top: 46px; width: 42px; height: 76px; background: var(--sky); }
  .name-plate .name { position: absolute; left: 150px; top: 18px; width: 680px; text-align: center; font-family: Arial, Helvetica, sans-serif; font-weight: 700; font-size: 122px; line-height: 170px; color: var(--brand-blue); }
  .name-plate .dot { position: absolute; left: 868px; top: 48px; width: 108px; height: 108px; border-radius: 50%; background: var(--brand-blue); }

  .base-strip { position: absolute; left: 0; top: 2500px; width: 1200px; height: 35px; background: var(--brand-blue); border-top: 8px solid var(--sky); }
</style>
</head>
<body>
<div class="brochure">
  <div class="top-bar"></div>

  <p class="intro">Dr. Halden is a highly trained specialised surgeon, in all areas of Endocrine, Breast and General Surgery.</p>

  <ul class="specialties">
    <li>Thyroid Surgery</li>
    <li class="two-line">Parathyroid surgery (including minimally invasive parathyroidectomy)</li>
    <li>Breast Cancer Benign breast lesions</li>
  </ul>

  <div class="stethoscope" role="img" aria-label="Blue stethoscope illustration"></div>

  <div class="surgery-panel">
    <svg width="1200" height="1345" viewBox="0 0 1200 1345" aria-hidden="true">
      <path d="M0 260 Q0 0 260 0 L1200 0 L1200 1345 L0 1345 Z" fill="var(--sky)"/>
      <path d="M0 300 Q0 58 260 58 L1200 58 L1200 1345 L0 1345 Z" fill="var(--brand-blue)"/>
    </svg>
  </div>

  <h2 class="panel-title">All areas of<br>general surgery</h2>

  <ul class="procedures">
    <li>Gallbladder surgery</li>
    <li>Hernia surgery</li>
    <li>Haemorrhoids</li>
    <li>Carpal Tunnel</li>
    <li>Vasectomy etc etc…</li>
  </ul>

  <div class="portrait" role="img" aria-label="Portrait photograph of the doctor in a dark jacket and checked shirt"></div>

  <div class="name-plate">
    <div class="tab"></div>
    <div class="name">Dr. Halden</div>
    <div class="dot"></div>
  </div>

  <div class="base-strip"></div>
</div>
</body>
</html>
```